Private Optometric Practice Needs new Presentation Folders/Stationary

We recently moved our office and are looking to refresh our presentation folders and stationary. I tend to prefer simple, clean designs. We are a full scope optometric practice provide high quality eyewear, custom contact lenses, along with emergency care and treatment for dry eyes. We communicate with a lot of other doctors and want to exude professionalism. I have attached 2 versions of our logo.

Target Market(s)

Familys

Industry/Entity Type

Eyecare

Font styles to use
Sans Serif

Colors
0054AA
0677BA
7BADD7
CADEEF
E8F1F8

Requirements
Nice to have
• Bifold, areas to put information about practice, welcome letter

```html
<!DOCTYPE html>
<html lang="en">
<head>
<meta charset="utf-8">
<title>Brightfield Eyecare – Presentation Folder and Letterhead</title>
<link rel="stylesheet" href="https://fonts.googleapis.com/css2?family=Cinzel:wght@400&family=Raleway:wght@400;500&family=Parisienne&display=swap">
<style>
  :root {
    --backdrop: #b9b8bd;
    --paper: #ffffff;
    --panel-shade: #f1f1f2;
    --ink-dark: #2c2c30;
    --ink-grey: #8d8d92;
    --ink-faint: #e6e6e8;
    --brand-blue: #0677ba;
  }
  * { box-sizing: border-box; margin: 0; padding: 0; }
  html, body { width: 1200px; height: 1000px; overflow: hidden; }
  body {
    background: var(--backdrop);
    font-family: "Raleway", Arial, sans-serif;
    position: relative;
  }

  /* ---------- Folder (open, flat) ---------- */
  .folder {
    position: absolute;
    left: 40px; top: 400px;
    width: 720px; height: 500px;
    display: flex;
    box-shadow: 0 6px 18px rgba(0,0,0,.18);
  }
  .folder-panel {
    position: relative;
    width: 360px; height: 500px;
    background: var(--paper);
  }
  .folder-panel--front { background: linear-gradient(180deg, var(--paper), var(--panel-shade)); }
  .folder-photo {
    position: absolute; left: 0; top: 0;
    width: 720px; height: 500px;
    pointer-events: none;
  }
  .folder-contact {
    position: absolute; left: 36px; bottom: 40px;
    font-size: 8px; letter-spacing: .08em; color: var(--ink-grey);
    line-height: 1.5; text-transform: uppercase;
  }
  .folder-contact .brand { margin-bottom: 14px; }
  .folder-contact .address { margin-bottom: 6px; }

  .tagline { position: absolute; }
  .tagline-lead {
    font-family: "Cinzel", Georgia, serif;
    font-size: 22px; letter-spacing: .04em; color: var(--ink-grey);
    line-height: 1.2;
  }
  .tagline-script {
    font-family: "Parisienne", cursive;
    font-size: 50px; color: var(--brand-blue);
    line-height: .9; margin-left: 36px;
  }
  .folder-tagline { left: 90px; top: 352px; }

  /* ---------- Brand name ---------- */
  .brand {
    display: flex; align-items: center; gap: 7px;
    font-family: "Raleway", Arial, sans-serif;
    font-weight: 500; text-transform: uppercase;
    letter-spacing: .2em; color: var(--ink-dark);
  }
  .brand-dot { border-radius: 50%; background: var(--brand-blue); flex: none; }
  .brand--folder { font-size: 12px; }
  .brand--folder .brand-dot { width: 12px; height: 12px; }
  .folder-brand { position: absolute; left: 150px; top: 448px; }

  /* ---------- Letterhead ---------- */
  .letterhead {
    position: absolute;
    left: 800px; top: 68px;
    width: 360px; height: 509px;
    background: var(--paper);
    box-shadow: 0 6px 18px rgba(0,0,0,.15);
  }
  .letterhead-rule {
    position: absolute; left: 0; right: 0; height: 3px;
    background: var(--ink-dark);
  }
  .letterhead-rule--top { top: 12px; }
  .letterhead-rule--bottom { bottom: 12px; }
  .letterhead-brand {
    position: absolute; top: 36px; left: 0; right: 0;
    display: flex; justify-content: center;
  }
  .brand--letter { font-size: 9px; }
  .brand--letter .brand-dot { width: 9px; height: 9px; }
  .letterhead-tagline { left: 26px; top: 220px; }
  .letterhead-tagline .tagline-lead { color: var(--ink-faint); font-size: 24px; }
  .letterhead-tagline .tagline-script { color: var(--ink-faint); font-size: 60px; margin-left: 70px; }
  .letterhead-footer {
    position: absolute; left: 22px; right: 22px; bottom: 28px;
    display: flex; justify-content: space-between;
    font-size: 7px; letter-spacing: .06em; color: var(--ink-grey);
    text-transform: uppercase; line-height: 1.5;
  }
  .contact-line { display: flex; align-items: center; gap: 5px; }
  .contact-line svg { width: 7px; height: 7px; fill: var(--ink-grey); flex: none; }
</style>
</head>
<body>

<section class="folder" aria-label="Presentation folder, open spread">
  <div class="folder-panel folder-panel--inside">
    <div class="folder-contact">
      <div class="brand brand--folder"><span class="brand-dot"></span>Brightfield Eyecare</div>
      <p class="address">1420 Harbor View Rd. Suite B<br>Lakeridge, MI 48000</p>
      <p class="contact-line">
        <svg viewBox="0 0 10 10"><path d="M2 0.5 L3.6 0.5 L4.3 3 L3.2 3.8 Q4.2 6 6.2 6.8 L7 5.7 L9.5 6.4 L9.5 8 Q9.5 9.5 8 9.5 Q0.5 9 0.5 2 Q0.5 0.5 2 0.5Z"/></svg>
        555-014-2290
      </p>
      <p class="contact-line">
        <svg viewBox="0 0 10 10"><circle cx="5" cy="5" r="4.3" fill="none" stroke="#8d8d92" stroke-width="1"/><path d="M0.7 5 H9.3 M5 0.7 Q2 5 5 9.3 Q8 5 5 0.7" fill="none" stroke="#8d8d92" stroke-width=".8"/></svg>
        mybrightfieldeyecare.com
      </p>
    </div>
  </div>
  <div class="folder-panel folder-panel--front">
    <div class="tagline folder-tagline">
      <p class="tagline-lead">Eyesight is</p>
      <p class="tagline-script">precious</p>
    </div>
    <div class="folder-brand brand brand--folder"><span class="brand-dot"></span>Brightfield Eyecare</div>
  </div>

  <svg class="folder-photo" viewBox="0 0 720 500" role="img"
       aria-label="Photo of a man sitting on a rock by the sea at sunset, a sailboat on the horizon, framed in a lens shape">
    <defs>
      <linearGradient id="sunset-sea" x1="0" y1="0" x2="0" y2="1">
        <stop offset="0" stop-color="#d9cfc4"/>
        <stop offset=".3" stop-color="#e3c39b"/>
        <stop offset=".55" stop-color="#8f8a84"/>
        <stop offset="1" stop-color="#3c4650"/>
      </linearGradient>
    </defs>
    <path d="M270 150 Q420 50 600 70 Q680 80 720 112 L720 238 Q640 330 560 335 Q360 330 270 150 Z" fill="url(#sunset-sea)"/>
  </svg>
</section>

<section class="letterhead" aria-label="Letterhead">
  <div class="letterhead-rule letterhead-rule--top"></div>
  <div class="letterhead-brand">
    <div class="brand brand--letter"><span class="brand-dot"></span>Brightfield Eyecare</div>
  </div>
  <div class="tagline letterhead-tagline">
    <p class="tagline-lead">Eyesight is</p>
    <p class="tagline-script">precious</p>
  </div>
  <footer class="letterhead-footer">
    <div>
      <p class="contact-line">
        <svg viewBox="0 0 10 10"><path d="M2 0.5 L3.6 0.5 L4.3 3 L3.2 3.8 Q4.2 6 6.2 6.8 L7 5.7 L9.5 6.4 L9.5 8 Q9.5 9.5 8 9.5 Q0.5 9 0.5 2 Q0.5 0.5 2 0.5Z"/></svg>
        555-014-2290
      </p>
      <p class="contact-line">
        <svg viewBox="0 0 10 10"><circle cx="5" cy="5" r="4.3" fill="none" stroke="#8d8d92" stroke-width="1"/><path d="M0.7 5 H9.3 M5 0.7 Q2 5 5 9.3 Q8 5 5 0.7" fill="none" stroke="#8d8d92" stroke-width=".8"/></svg>
        www.mybrightfieldeyecare.com
      </p>
    </div>
    <p>1420 Harbor View Rd. Suite B<br>Lakeridge, MI 48000</p>
  </footer>
  <div class="letterhead-rule letterhead-rule--bottom"></div>
</section>

</body>
</html>
```